Open Now Poster for Retail Shop windows.

To design a poster to be printed to put on the windows of our retail stores to tell customers that we are open. Size is to be 590mm W x 840mm H supplied as a pdf. Design should incorporate our logo as well as other elements which indicate the style of our shop which is Womens Beach, Resort & Casual Clothing, Swimwear and Accessories. I would like the design to incorporate the words "Open Now" in some form in large lettering. I would also like the poster to be timeless and able to be used for other wording, so no images would be preferable.

Target Market(s)

Womens Beach, Resort & Casual Clothing, Swimwear and Accessories

Industry/Entity Type

Retail

Colors
e34297

Requirements
Must have
• words "Open Now". as well as our logo.

```html
<!DOCTYPE html>
<html lang="en">
<head>
<meta charset="utf-8">
<title>Open Now – Window Poster</title>
<link rel="stylesheet" href="https://fonts.googleapis.com/css2?family=Questrial&display=swap">
<style>
  :root {
    --stage: #a8a9ac;
    --paper-light: #fbe4eb;
    --paper-edge: #f3d1d2;
    --brand-pink: #e40a80;
    --hat-pink: #e2127f;
    --lens-dark: #4a3a3a;
    --dress-top: #e0147f;
    --dress-mid: #f065a8;
    --shoe-dark: #3a1a1f;
  }
  html, body {
    margin: 0;
    padding: 0;
    width: 1200px;
    height: 1200px;
    overflow: hidden;
    background: var(--stage);
  }
  .canvas {
    width: 1200px;
    height: 1200px;
    display: flex;
    align-items: center;
    justify-content: center;
  }
  .poster {
    display: block;
    width: 842px;
    height: 1200px;
  }
  .poster-text {
    font-family: "Questrial", "Century Gothic", sans-serif;
    fill: var(--brand-pink);
  }
</style>
</head>
<body>
<main class="canvas">
  <svg class="poster" viewBox="0 0 877 1250" xmlns="http://www.w3.org/2000/svg">
    <defs>
      <radialGradient id="paper-glow" cx="0.5" cy="0.48" r="0.65">
        <stop offset="0" stop-color="var(--paper-light)"/>
        <stop offset="1" stop-color="var(--paper-edge)"/>
      </radialGradient>
      <linearGradient id="dress-tone" x1="0" y1="0" x2="0" y2="1">
        <stop offset="0" stop-color="var(--dress-top)"/>
        <stop offset="0.55" stop-color="var(--dress-mid)"/>
        <stop offset="1" stop-color="var(--dress-top)"/>
      </linearGradient>
      <linearGradient id="shoe-tone" x1="0" y1="0" x2="0" y2="1">
        <stop offset="0" stop-color="#f4eef0"/>
        <stop offset="1" stop-color="var(--shoe-dark)"/>
      </linearGradient>
    </defs>

    <rect class="poster-paper" width="877" height="1250" fill="url(#paper-glow)"/>

    <!-- Headline running up the page -->
    <text class="poster-text headline-vertical" transform="translate(347 1013) rotate(-90)"
          font-size="226" textLength="907" lengthAdjust="spacingAndGlyphs">pen now</text>

    <!-- Brand name -->
    <text class="poster-text brand-name" x="94" y="1150"
          font-size="232" textLength="655" lengthAdjust="spacingAndGlyphs">so chic</text>
    <text class="poster-text brand-registered" x="756" y="1018" font-size="26">®</text>

    <!-- Accessory illustrations -->
    <rect class="art-hat" x="504" y="68" width="190" height="163" rx="60"
          fill="var(--hat-pink)" role="img" aria-label="Illustration of a wide-brim pink sun hat with a white ribbon"/>
    <rect class="art-sunglasses" x="531" y="261" width="136" height="63" rx="31"
          fill="var(--lens-dark)" role="img" aria-label="Illustration of round sunglasses with pink and white frames"/>
    <rect class="art-dress" x="481" y="362" width="235" height="400" rx="18"
          fill="url(#dress-tone)" role="img" aria-label="Illustration of a sleeveless pink polka-dot summer dress"/>
    <rect class="art-shoes" x="547" y="793" width="102" height="171" rx="30"
          fill="url(#shoe-tone)" role="img" aria-label="Illustration of a pair of white flat shoes with pink bows"/>
  </svg>
</main>
</body>
</html>
```